Snooker/Billiards/CueSports Website - winner, second and 3rd paid!

We are looking to launch a website related to “cuesports”, especially snooker. Snooker is a popular sport in The UK and worldwide.

We are looking to build 2 pages with you for this contest

- the homepage
- and a page which will be used FOR EACH player we are working with and promoting (More below)

At the moment we have no idea about the design but it should be classy, ie. maybe similar to many of the high end fashion sites - maybe this kind of look?

https://www.vostrafind.co.uk/search?q=high+end+websites&espv=2&biw=1396&bih=694&source=lnms&tbm=isch&sa=X&ved=0ahUKEwiq6MaprYvPAhVoKcAKHW8mCiUQ_AUIBigB#tbm=isch&q=classy+websites

UNLESS THIS IS COMPLETELY THE WRONG IDEA FOR WHAT WE ARE DOING, we will leave it up to you to show us some of your best ideas and help us succeed!

We are more interested in the layout and design than the text at this stage. We can add gthe main text later with your help or by ourselves, but Design, look and feel is what we want to see for this contes. Obviously if you have any questions we will give you regular feedback during the time of this contest.

This will be an ecommerce site but we expect to get to the shopping cart stage in about a month

Our main marketing tool will be our website.

There are 3 core parts to our business in priority order:

1. Sales of Snooker/Billiards Equipment
We will be selling everything from the smallest items, snooker tips, chalk, to snooker cues (sticks) all the way to Major items such as snooker tables.

Here are some typical sites that sell snooker related equipment:

http://www.peterwelbeckbaizehall.com/
http://www.cuefervora.co.uk/
http://www.qrtbaize.co.uk/

2. Sale of our own branded fashion accessories: T’shirts, Caps, jackets, cologne etc etc

3. Our booking section, where we will promote famous snooker players and other sports stars for exhibitions, after dinner speaking, golf days, etc
(probably 1 page per player in the booking section with a picture, brief bio, summary of the kind of things they can be booked for and perhaps a tarrif sheet, though we may not publish this information online and prefer to ask people to contact us if they wish to book a player

Target Markets

Mainly the UK and Europe, but snooker is becoming increasingly popular in China

Demographics are mostly males aged 16 and 40

Logo Design (separate contest at a later time)

1. The design must project a sense of professionalism and have a high class feel

2. Must Have Priorities:

- Modern, professional and friendly.
- Strong emphasis on usability.
- mobile friendly - responsive

3. Should not Have:

- An anonymous cold and corporate feel.
- A too busy feel.

4. The winner of this design contest will also be awarded a freelance project to help us further develop/complete the site.

Thank You everyone and Good luck !

18-40 mainly

2 page

• - Modern, professional and friendly.
• - Strong emphasis on usability.
• - mobile friendly - responsive
• - An anonymous cold and corporate feel.
• - A too busy feel.

```html
<!DOCTYPE html>
<html lang="en">
<head>
<meta charset="utf-8">
<title>Marlow Cue Sports</title>
<link href="https://fonts.googleapis.com/css2?family=Raleway:ital,wght@0,400;0,500;0,600;0,800;1,500&family=Kaushan+Script&display=swap" rel="stylesheet">
<style>
:root{
  --black:#000;
  --footer:#0b0b0b;
  --gold:#b09a4e;
  --gold-light:#c9b465;
  --gold-dark:#8e7a33;
  --white:#fff;
  --muted:#b5b5b5;
  --rule:#2a2a2a;
}
*{margin:0;padding:0;box-sizing:border-box}
html,body{width:953px;height:1200px;overflow:hidden;background:var(--black)}
body{position:relative;font-family:'Raleway',sans-serif;color:var(--white)}
.abs{position:absolute}

/* hero */
.hero-photo{left:0;top:0;width:953px;height:520px;
  background:radial-gradient(ellipse at 60% 70%,#3a2a26 0%,#1d2a27 40%,#0f1a18 75%),#14201e}
.hero-photo::after{content:"";position:absolute;inset:0;background:linear-gradient(180deg,rgba(0,0,0,.1),rgba(0,0,0,.35))}
.top-line{left:0;top:0;width:953px;height:3px;background:var(--gold)}
.header-shape{left:0;top:0}
.tab{top:0;height:28px;background:var(--gold);color:var(--white);font-size:8.5px;font-weight:600;
  display:flex;align-items:center;justify-content:center;gap:5px;border-radius:0 0 22px 22px}
.tab-create{left:566px;width:134px}
.tab-register{left:728px;width:136px}
.tab svg{width:8px;height:8px}
.logo{left:78px;top:26px;font-size:25px;font-weight:600;color:var(--gold-light);letter-spacing:.2px}
.main-nav{top:57px;right:79px;display:flex}
.main-nav a{color:var(--white);text-decoration:none;font-size:11px;font-weight:500;margin-left:43px}
.hero-title{left:78px;top:240px;font-size:34px;font-weight:800;letter-spacing:.3px}
.hero-sub{left:78px;top:290px;width:380px;font-size:14px;font-style:italic;font-weight:500;line-height:22px}
.btn{background:linear-gradient(180deg,var(--gold-light),var(--gold-dark));color:var(--white);
  font-weight:600;display:flex;align-items:center;justify-content:center;text-decoration:none}
.hero-btn{left:78px;top:352px;width:123px;height:37px;font-size:11.5px}
.dots{left:826px;top:480px;display:flex;gap:6px}
.dots i{width:6px;height:6px;border-radius:50%;background:#ccc}
.dots i:first-child{background:var(--gold-light)}

/* services */
.section-title{left:0;width:953px;top:560px;text-align:center;font-family:'Kaushan Script',cursive;font-size:25px;font-weight:400}
.section-title span{color:var(--gold-light)}
.section-intro{left:130px;width:693px;top:598px;text-align:center;font-size:10.5px;line-height:18px;color:#ddd}
.card{top:655px;width:251px;height:177px;border:2px solid #555}
.card-equipment{left:78px;background:linear-gradient(135deg,#15795e,#0c5a45)}
.card-fashion{left:351px;background:linear-gradient(135deg,#5a3326,#b06a48 60%,#2f4d45)}
.card-booking{left:625px;background:linear-gradient(135deg,#8a6a44,#e4d6bd 70%,#c4a880)}
.card-panel{position:absolute;background:rgba(0,0,0,.78);text-align:center;padding-top:10px}
.card-panel small{display:block;font-size:11px;color:var(--gold-light)}
.card-panel strong{display:block;font-size:15px;font-weight:600;color:var(--gold-light);margin-top:2px}
.card-panel p{font-size:10.4px;line-height:19px;margin-top:3px;color:var(--white);padding:0 10px}

/* footer */
.footer-bg{left:0;top:832px;width:953px;height:368px}
.footer-logo{left:78px;top:938px;font-size:25px;font-weight:600;color:var(--gold-light)}
.follow{left:663px;top:953px;font-size:12px;font-weight:600;display:flex;align-items:center;gap:4px}
.follow i{width:23px;height:23px;border:1px solid #ddd;border-radius:50%;display:flex;align-items:center;justify-content:center}
.follow i::after{content:"";width:7px;height:7px;border-radius:50%;background:#ddd}
.follow i:first-of-type{margin-left:2px}
.footer-rule{left:78px;top:987px;width:797px;height:1px;background:var(--rule)}
.col{top:1011px}
.col h4{font-size:12px;font-weight:600;margin-bottom:14px}
.col a,.col li{color:var(--muted);font-size:10.5px;text-decoration:none;list-style:none;line-height:20px;display:block}
.col-nav{left:78px}
.col-nav .pair{display:grid;grid-template-columns:64px 60px}
.col-links{left:239px}
.col-contact{left:389px;width:250px}
.col-contact li{display:flex;gap:8px;margin-bottom:9px;line-height:19px}
.col-contact svg{width:11px;height:11px;flex:none;margin-top:4px}
.col-news{left:655px}
.email-field{width:219px;height:30px;background:var(--white);border-radius:3px;color:#999;font-size:10px;padding:9px 10px}
.col .sub-btn{display:flex;align-items:center;justify-content:center;width:103px;height:36px;margin-top:5px;
  font-size:10.5px;font-weight:600;line-height:1;color:var(--white);border-radius:2px}
.copyright{left:0;top:1161px;width:953px;height:39px;background:var(--gold);display:flex;align-items:center;justify-content:center;font-size:10px}
</style>
</head>
<body>

<div class="abs hero-photo" role="img" aria-label="Close-up photograph of billiard balls racked on green baize"></div>

<svg class="abs header-shape" width="953" height="200" viewBox="0 0 953 200">
  <path d="M0,0 H953 V78 Q820,138 650,128 Q540,120 470,118 Q260,80 0,135 Z" fill="#000"/>
  <path d="M0,190 Q120,100 470,118 Q230,70 0,140 Z" fill="#fff"/>
  <path d="M0,190 Q140,110 470,118 Q240,80 0,150 Z" fill="var(--gold)"/>
</svg>
<div class="abs top-line"></div>

<div class="abs tab tab-create">
  <svg viewBox="0 0 10 10"><rect x="1" y="2" width="7" height="7" fill="none" stroke="#fff" stroke-width="1.2"/><path d="M4 6 L9 1" stroke="#fff" stroke-width="1.4"/></svg>
  CREATE AN ACCOUNT
</div>
<div class="abs tab tab-register">
  <svg viewBox="0 0 10 10"><circle cx="5" cy="3" r="2.2" fill="#fff"/><path d="M1 10 Q5 3 9 10 Z" fill="#fff"/></svg>
  REGISTER
</div>

<div class="abs logo">Marlow Cue Sports</div>
<nav class="abs main-nav">
  <a href="#">HOME</a><a href="#">ABOUT</a><a href="#">SERVICES</a><a href="#">TESTIMONIALS</a><a href="#">BLOG</a><a href="#">CONTACT</a>
</nav>

<h1 class="abs hero-title">SNOOKER AND BILLIARDS</h1>
<p class="abs hero-sub">Nemo enim ipsam voluptatem quia voluptas sit aspernatur aut odit aut fugit, sed quia ratione voluptatem...</p>
<a class="abs btn hero-btn">GET START TODAY</a>
<div class="abs dots"><i></i><i></i><i></i><i></i></div>

<h2 class="abs section-title">Our Feature <span>Services</span></h2>
<p class="abs section-intro">Sed ut perspiciatis unde omnis iste natus error sit voluptatem accusantium doloremque laudantium, totam rem aperiam, eaque ipsa quae ab illo inventore veritatis et quasi architecto beatae vitae dicta sunt explicabo. Nemo enim ipsam</p>

<div class="abs card card-equipment" role="img" aria-label="Photograph of a cue, chalk and coloured balls on green baize">
  <div class="card-panel" style="left:29px;top:60px;width:191px;height:54px"><small>Sales of Snooker</small><strong>BILLIARDS EQUIPMENT</strong></div>
</div>
<div class="abs card card-fashion" role="img" aria-label="Photograph of young people playing pool in a bar">
  <div class="card-panel" style="left:19px;top:48px;width:210px;height:76px"><small>Sale of our own Branded</small><strong>FASHION ACCESSORIES</strong><p>T'shirts, Caps, jackets, cologne etc etc</p></div>
</div>
<div class="abs card card-booking" role="img" aria-label="Photograph of a group of friends around a pool table">
  <div class="card-panel" style="left:18px;top:28px;width:212px;height:119px"><strong>OUR BOOKING SECTION</strong><p>where we will promote famous snooker players and other sports stars for exhibitions, after dinner speaking, golf days, etc</p></div>
</div>

<svg class="abs footer-bg" width="953" height="368" viewBox="0 0 953 368">
  <path d="M0,80 Q250,50 480,70 Q800,110 953,0 V368 H0 Z" fill="var(--footer)"/>
  <path d="M480,70 Q800,130 953,30 V0 Q800,100 480,70 Z" fill="#fff"/>
  <path d="M480,70 Q800,118 953,22 V0 Q800,95 480,70 Z" fill="var(--gold)"/>
</svg>

<div class="abs footer-logo">Marlow Cue Sports</div>
<div class="abs follow">FOLLOW US :<i></i><i></i><i></i><i></i><i></i></div>
<div class="abs footer-rule"></div>

<div class="abs col col-nav">
  <h4>NAVIGATION</h4>
  <div class="pair"><a href="#">Home</a><a href="#">Blog</a><a href="#">About</a><a href="#">Contact</a><a href="#">Services</a><span></span><a href="#">Testimonials</a></div>
</div>
<div class="abs col col-links">
  <h4>LINKS</h4>
  <a href="#">Terms &amp; Conditions</a><a href="#">Privacy Policy</a><a href="#">Site Map</a><a href="#">Disclaimer</a>
</div>
<div class="abs col col-contact">
  <h4>CONTACT INFO</h4>
  <ul>
    <li><svg viewBox="0 0 10 10"><path d="M5 10 L1.6 5 A4 4 0 1 1 8.4 5 Z" fill="#aaa"/><circle cx="5" cy="3.8" r="1.4" fill="#0b0b0b"/></svg>544 Marlow Cue Sports, Company Name, Street, City, Country-5656</li>
    <li><svg viewBox="0 0 10 10"><path d="M1 1 L3.5 1 L4.5 3.5 L3 4.5 Q4.5 7 6.5 7.5 L7.5 6 L10 7 L10 9.5 Q4 10 1 3 Z" fill="#aaa"/></svg>Help :000-0000-00000000</li>
    <li><svg viewBox="0 0 10 10"><rect x="0.5" y="2" width="9" height="6.5" fill="#aaa"/><path d="M0.5 2 L5 6 L9.5 2" stroke="#0b0b0b" fill="none"/></svg>info@marlowcuesports.com</li>
  </ul>
</div>
<div class="abs col col-news">
  <h4>NEWSLETTER</h4>
  <div class="email-field">Enter e-mail address</div>
  <a class="btn sub-btn">SUBSCRIBE</a>
</div>

<div class="abs copyright">Copyrights©Marlow Cue Sports 2016 | Allrights Reserved.</div>

</body>
</html>
```